Serlivo Business Cards

We need new Business Cards for our startup. It just launched.It is working in the high-end it-market. Specifically in the cloud area. We are a hybrid cloud company. The company logo is attached. We are a Swiss based company. Information visible on the card is: 1. Logo 2. Company Name: Serlivo AG 3. Subtitle: Hybrid Clouds. 3. Name: Tobias Ferrand 4. Adress: Lindenhofweg 14a, 8217 Rhenwil, Switzerland 5. Email: tobias@serlivo-mail.ch. 6. Mobile: +41 79 386 42 15. It should be a grey/white design. Similar to the attached logo. It should have class, high-quality but not too much color and no gold used.
Updates

I forgot to add my Position. Please use Founder / CEO. thanks tobias

Industry/Entity Type

Business

```html
<!DOCTYPE html>
<html lang="en">
<head>
<meta charset="utf-8">
<title>Serlivo AG – Business Card</title>
<link rel="stylesheet" href="https://fonts.googleapis.com/css2?family=Lato:wght@300;400;700&display=swap">
<style>
  :root {
    --backdrop: #e4e4e4;
    --card: #ffffff;
    --ink-strong: #1f1f1f;
    --ink-soft: #5a5a5a;
    --ink-muted: #6e6e6e;
    --tab: #6b6b6b;
    --icon: #3d3d3d;
  }
  * { box-sizing: border-box; margin: 0; padding: 0; }
  html, body {
    width: 1200px;
    height: 888px;
    overflow: hidden;
    background: var(--backdrop);
    font-family: "Lato", sans-serif;
  }
  .business-card {
    position: absolute;
    left: 100px;
    top: 184px;
    width: 1000px;
    height: 520px;
    background: var(--card);
    box-shadow: 0 10px 30px rgba(0, 0, 0, 0.18);
    overflow: hidden;
  }
  .edge-tab {
    position: absolute;
    left: -22px;
    top: 300px;
    width: 52px;
    height: 96px;
    border-radius: 18px;
    background: var(--tab);
  }
  .brand {
    position: absolute;
    left: 340px;
    top: 78px;
    display: flex;
    align-items: center;
    gap: 26px;
  }
  .brand-dot {
    width: 22px;
    height: 22px;
    border-radius: 50%;
    background: var(--ink-muted);
  }
  .brand-name {
    font-weight: 300;
    font-size: 54px;
    letter-spacing: 0.42em;
    color: var(--ink-soft);
    text-transform: uppercase;
  }
  .holder {
    position: absolute;
    left: 130px;
    top: 312px;
  }
  .holder-name {
    font-weight: 700;
    font-size: 34px;
    color: var(--ink-strong);
    letter-spacing: 0.01em;
  }
  .holder-role {
    margin-top: 4px;
    font-weight: 400;
    font-size: 28px;
    color: var(--ink-muted);
  }
  .contact-list {
    position: absolute;
    left: 500px;
    top: 262px;
    list-style: none;
  }
  .contact-item {
    display: flex;
    align-items: center;
    gap: 12px;
    height: 30px;
    font-size: 21px;
    color: var(--ink-strong);
    white-space: nowrap;
  }
  .contact-icon {
    width: 18px;
    height: 18px;
    flex: none;
    fill: var(--icon);
  }
</style>
</head>
<body>
  <article class="business-card">
    <div class="edge-tab"></div>

    <header class="brand">
      <span class="brand-dot"></span>
      <span class="brand-name">Serlivo</span>
    </header>

    <section class="holder">
      <h1 class="holder-name">Tobias Ferrand</h1>
      <p class="holder-role">Founder / CEO</p>
    </section>

    <ul class="contact-list">
      <li class="contact-item">
        <svg class="contact-icon" viewBox="0 0 24 24" aria-hidden="true">
          <path d="M6.6 10.8a15.1 15.1 0 0 0 6.6 6.6l2.2-2.2c.3-.3.7-.4 1-.2 1.1.4 2.3.6 3.6.6.6 0 1 .4 1 1V20c0 .6-.4 1-1 1C10.6 21 3 13.4 3 4c0-.6.4-1 1-1h3.5c.6 0 1 .4 1 1 0 1.3.2 2.5.6 3.6.1.3 0 .7-.2 1z"/>
        </svg>
        <span>+41 79 386 42 15</span>
      </li>
      <li class="contact-item">
        <svg class="contact-icon" viewBox="0 0 24 24" aria-hidden="true">
          <path d="M2 5h20v14H2zM4 7v.5l8 5 8-5V7l-8 5z"/>
        </svg>
        <span>tobias@serlivo-mail.ch</span>
      </li>
      <li class="contact-item">
        <svg class="contact-icon" viewBox="0 0 24 24" aria-hidden="true">
          <path d="M12 2a7 7 0 0 0-7 7c0 5.2 7 13 7 13s7-7.8 7-13a7 7 0 0 0-7-7zm0 9.5A2.5 2.5 0 1 1 12 6.5a2.5 2.5 0 0 1 0 5z"/>
        </svg>
        <span>Lindenhofweg 14a, 8217 Rhenwil, Switzerland</span>
      </li>
    </ul>
  </article>
</body>
</html>
```